Existing Cardiology Practice now offering New PET MPI Services Brochure

We are a private group cardiology practice that is opening a new PET MPI services. We would like a brochure that emphasizes our New PET MPI and what that is as well as all of our other services offered at our practice. Minimally The front of the brochure should have the physician group picture with their names, our clinic logo, the PET MPI, our address, phone, fax, website. The inside should include the information regarding what the PET MPI is (included as an attachment to this project). The back should have the map with our location on it, and all the other services offered as written on the attachment to this project. When listing the services on the back , please make sure you spell everything correctly and list them accordingly. The names of the physicians in order from Left to Right are Varun Mehrotra, MD, Girish Kandalkar, MD, Manoj Iyer, MD, Tarun Iyer, MD. The brochure should be 8 1/2 inches in height and when opened be 11 inches in length. It will be a bifold brochure.

Target Market(s)

Healthcare Providers, healthcare facilities, patients.

Industry/Entity Type

Health Care

Font styles to use
Sans Serif

Requirements
Must have
• Physician Group Picture, Logo, New PET MPI, address, phone 714-368-2217, Fax 714-368-2218. Web address www.crestlinecardio.com. Services Offered listing, PET MPI information, Map Picture.
Nice to have
• Open to suggestions
Should not have
• Not sure

```html
<!DOCTYPE html>
<html lang="en">
<head>
<meta charset="utf-8">
<title>Crestline Heart – Cardiac PET MPI Brochure</title>
<link href="https://fonts.googleapis.com/css2?family=Montserrat:wght@400;500;600;700;800&family=Source+Sans+3:wght@400;600&family=Roboto+Condensed:wght@500;600&display=swap" rel="stylesheet">
<style>
:root{
  --red:#a8262e;
  --band:#a3353b;
  --frame:#7c0f1b;
  --ink:#1b1b1b;
  --mist:#f4f4f4;
  --green:#23402d;
  --white:#ffffff;
}
*{box-sizing:border-box;margin:0;padding:0}
html,body{width:847px;height:1200px;overflow:hidden;background:#fff}
body{position:relative;font-family:"Source Sans 3",sans-serif;color:var(--ink)}
.abs{position:absolute}
.accent{color:var(--red)}

/* inside spread */
.intro{left:33px;top:32px;width:220px}
.intro h2{font-family:"Montserrat",sans-serif;font-size:12px;font-weight:700;margin-bottom:8px}
.intro h2 .accent{font-weight:500}
.acronym{font-family:"Montserrat",sans-serif;font-size:10px;line-height:17px}
.intro p{font-size:9px;line-height:11.2px;margin-top:11px}
.why{left:33px;top:266px;width:230px}
.why h2{font-family:"Montserrat",sans-serif;font-size:12px;font-weight:700}
.why p{font-size:6.4px;line-height:14px;margin-top:8px}
.benefits{left:6px;top:353px;width:273px;height:238px;background:var(--band);color:#fff;padding:22px 0 0 40px}
.benefits ul{list-style:disc;font-family:"Montserrat",sans-serif;font-size:6.9px;line-height:16.3px}
.benefits li{padding-left:12px}

.expect{left:284px;top:3px;width:278px;height:585px;background:var(--mist);padding:32px 40px 0 26px}
.expect h2{font-family:"Montserrat",sans-serif;font-size:11.5px;font-weight:700;color:var(--red);margin-bottom:22px}
.expect p{font-size:7.8px;line-height:16.7px;margin-bottom:16.5px}

.services-title{left:562px;top:72px;width:285px;text-align:center;font-family:"Montserrat",sans-serif;font-weight:700;font-size:23px;line-height:38px}
.services-title .dark{color:var(--ink)}
.services-list{left:590px;top:160px;width:240px;display:grid;grid-template-columns:1fr 1fr;column-gap:10px;list-style:disc;font-family:"Montserrat",sans-serif;font-size:7.4px;line-height:13px;padding-left:10px}
.services-list li::marker{color:var(--red)}
.safety-band{left:562px;top:353px;width:279px;height:238px;background:var(--band)}
.photo-frame{left:567px;top:222px;width:274px;height:194px;background:var(--frame);padding:5px}
.photo-fill{width:100%;height:100%}
.safety{left:591px;top:436px;width:232px;color:#fff}
.safety h3{font-family:"Montserrat",sans-serif;font-weight:700;font-size:20px;display:inline-block;border-bottom:2px solid #fff;line-height:22px;margin-bottom:8px}
.safety p{font-family:"Montserrat",sans-serif;font-size:9.5px;line-height:13px}

/* outside spread */
.outside{left:6px;top:600px;width:834px;height:591px;background:#fff;border-top:10px solid var(--band);box-shadow:0 0 3px rgba(0,0,0,.25)}
.outside-band{left:6px;top:953px;width:834px;height:238px;background:var(--band)}
.panel-head{font-family:"Montserrat",sans-serif;font-weight:800;font-size:22px;color:var(--red);letter-spacing:.6px;text-align:center}
.doctor{position:absolute;left:35px;width:225px;height:44px}
.avatar{position:absolute;left:0;top:0;width:40px;height:40px;border-radius:50%}
.doctor h4{position:absolute;left:52px;top:0;font-family:"Montserrat",sans-serif;font-weight:700;font-size:10px;color:var(--red)}
.doctor p{position:absolute;left:53px;top:14px;width:172px;font-size:8px;line-height:11.5px;text-align:justify}
.hours{left:284px;top:702px;width:278px;text-align:center;font-family:"Roboto Condensed",sans-serif;font-weight:600;font-size:20px;line-height:23px;color:var(--green)}
.icons{left:388px;top:761px;width:80px;height:16px}
.phones{left:284px;top:782px;width:278px;text-align:center;font-family:"Montserrat",sans-serif;font-weight:500;font-size:18px;line-height:25px}
.phones .label{font-size:10px;font-weight:600;color:var(--red);margin-right:5px}
.address{left:284px;top:836px;width:278px;text-align:center;font-family:"Montserrat",sans-serif;font-weight:500;font-size:10.4px;line-height:14px}
.address .web{font-weight:600;color:var(--red)}
.brand{left:618px;top:650px;display:flex;align-items:center;gap:7px}
.brand-dot{width:16px;height:16px;border-radius:50%;background:var(--red)}
.brand-name{font-family:"Montserrat",sans-serif;font-weight:700;font-size:17px;color:var(--red);letter-spacing:.5px}
.welcome{left:562px;top:736px;width:278px;text-align:center}
.welcome .hello{font-family:"Montserrat",sans-serif;font-weight:400;font-size:20px;display:inline-block;border-bottom:1px solid var(--ink);line-height:22px}
.welcome .name{font-family:"Montserrat",sans-serif;font-weight:700;font-size:21px;color:var(--red);margin-top:4px}
.welcome p{font-family:"Montserrat",sans-serif;font-size:9.8px;line-height:12px;margin-top:20px;padding:0 24px}
.card-frame{position:absolute;top:885px;width:219px;height:217px;background:var(--frame);padding:8px}
.caption{position:absolute;top:1125px;width:230px;text-align:center;color:#fff;font-family:"Montserrat",sans-serif;font-size:10px;line-height:12px}
</style>
</head>
<body>

<!-- Inside: what is PET MPI -->
<section class="abs intro">
  <h2><span class="accent">What is</span> Cardiac PET MPI?</h2>
  <div class="acronym"><span class="accent">PET -</span> Positron Emission Tomography<br><span class="accent">MPI -</span> Myocardial Perfusion Imaging</div>
  <p>A cardiac PET MPI exam provides accuracy, excellent quality, and the ability to detect disease before symptoms are present. This exam can diagnose cardiac disease with greater certainty and lower radiation exposure than traditional stress testing and is the gold standard for diagnosing coronary heart disease.</p>
  <p>We use this exam to evaluate the health of your heart by measuring the blood flow it receives. The results of this exam determine if treatment is needed or to manage your current treatment.</p>
</section>

<section class="abs why">
  <h2><span class="accent">WHY CHOOSE</span> CARDIAC PET MPI?</h2>
  <p>Patients benefit from a cardiac PET MPI exam for a variety of reasons,<br>some of them are:</p>
</section>

<section class="abs benefits">
  <ul>
    <li>Breast implants, large chest</li>
    <li>High-risk patients</li>
    <li>Known or suspected coronary artery disease</li>
    <li>Large body habitus, high BMI</li>
    <li>Prior poor-quality stress imaging study</li>
    <li>Requires pharmacologic stress imaging</li>
    <li>Time-sensitive, emergent</li>
    <li>Unable to exercise</li>
    <li>Young patients with coronary artery disease</li>
    <li>The need for a more accurate test</li>
  </ul>
</section>

<section class="abs expect">
  <h2>WHAT TO EXPECT:</h2>
  <p>Most cardiac PET exams take less than one hour; however, a longer exam should not be cause for concern. Upon arrival, our team will register you and review your medical history. Please be sure to report all medications you are taking.</p>
  <p>Trained medical personnel will be with you throughout your exam.</p>
  <p>An intravenous line will be placed in a vein in your arm to allow the administration of medication during the exam</p>
  <p>Small pads called electrodes will be placed on your chest to monitor the electrical activity of your heart throughout the study. Your blood pressure, heart rate, and electrocardiogram are monitored before, during, and after the test.</p>
  <p>You will be asked to lie down on a padded, comfortable scanning table developed especially for the PET camera. During your PET scan, the majority of your body is outside the scanner; this is not a full-body scan. If you're claustrophobic, please take your medication 30 minutes before your scan.</p>
  <p>In most cases, you may leave as soon as your cardiac PET MPI study is complete. You will be able to eat, drink, and return to your normal daily activities.</p>
</section>

<h1 class="abs services-title"><span class="accent">Hospital Services</span><br><span class="dark">Provided</span></h1>
<ul class="abs services-list">
  <li>Cardiac PET MPI (New)</li>
  <li>Echocardiography</li>
  <li>Nuclear Stress Testing</li>
  <li>Holter Monitoring</li>
  <li>Vascular Ultrasound</li>
  <li>EKG / ECG</li>
</ul>
<div class="abs safety-band"></div>
<div class="abs photo-frame">
  <div class="photo-fill" role="img" aria-label="Photo of two women chatting over coffee in a kitchen" style="background:linear-gradient(120deg,#3a3634,#8a7a6c 55%,#c9c3bb)"></div>
</div>
<section class="abs safety">
  <h3>SAFETY</h3>
  <p>Cardiac PET MPI scans are a safe and effective diagnostic imaging test. The tracer used is not a dye or contrast and results in minimal radiation exposure and enables a far</p>
</section>

<!-- Outside -->
<div class="abs outside"></div>
<div class="abs outside-band"></div>

<h2 class="abs panel-head" style="left:33px;top:648px;width:222px">OUR PHYSICIAN</h2>
<div class="doctor" style="top:688px">
  <div class="avatar" role="img" aria-label="Portrait of Dr. Varun Mehrotra" style="background:linear-gradient(#e3e0dc,#6a5f58)"></div>
  <h4>VARUN MEHROTRA, MD</h4>
  <p>At Crestline Heart we strive to provide the highest level and quality of cardiac care..</p>
</div>
<div class="doctor" style="top:735px">
  <div class="avatar" role="img" aria-label="Portrait of Dr. Girish Kandalkar" style="background:linear-gradient(#dfe3e6,#5b6168)"></div>
  <h4>GIRISH KANDALKAR, MD</h4>
  <p>At Crestline Heart we strive to provide the highest level and quality of cardiac care..</p>
</div>
<div class="doctor" style="top:782px">
  <div class="avatar" role="img" aria-label="Portrait of Dr. Manoj Iyer" style="background:linear-gradient(#cfd8e0,#b07b5a)"></div>
  <h4>MANOJ IYER, MD</h4>
  <p>At Crestline Heart we strive to provide the highest level and quality of cardiac care..</p>
</div>
<div class="doctor" style="top:829px">
  <div class="avatar" role="img" aria-label="Portrait of Dr. Tarun Iyer" style="background:linear-gradient(#2c3a52,#1a2233)"></div>
  <h4>TARUN IYER, MD</h4>
  <p>At Crestline Heart we strive to provide the highest level and quality of cardiac care..</p>
</div>

<h2 class="abs panel-head" style="left:284px;top:648px;width:278px">GET IN TOUCH</h2>
<div class="abs hours">Open Everyday<br>From 7 AM to 8 PM</div>
<svg class="abs icons" viewBox="0 0 80 16" aria-hidden="true">
  <g fill="var(--red)">
    <path d="M3 2c1-1 2-1 3 0l2 3c.5 1 0 1.6-.8 2.2.8 1.8 2 3 3.8 3.8.6-.8 1.2-1.3 2.2-.8l2 1.5c1 .8 1 1.8 0 2.8-2 2-6 0-9-3S1 4 3 2z"/>
    <rect x="32" y="1" width="10" height="4"/><rect x="29" y="5" width="16" height="7" rx="1.5"/><rect x="32" y="10" width="10" height="5" fill="#fff" stroke="var(--red)" stroke-width="1.5"/>
    <path d="M64 1l9 7.5h-2.5V15h-4.5v-4.5h-4V15h-4.5V8.5H55z"/>
  </g>
</svg>
<div class="abs phones"><span class="label">PH</span>714-368-2217<br><span class="label">FAX</span>714-368-2218</div>
<div class="abs address">418, 3<sup>rd</sup> Floor, Harbor Lane Street, NY 45012<br><span class="web">www.crestlinecardio.com</span></div>

<div class="abs brand">
  <span class="brand-dot"></span>
  <span class="brand-name">CRESTLINE HEART</span>
</div>
<section class="abs welcome">
  <div class="hello">Welcome to</div>
  <div class="name">CRESTLINE HEART</div>
  <p>at Crestline Heart we Strive to provide the highest level and Quality of cardiac care Available</p>
</section>

<div class="card-frame" style="left:33px">
  <div class="photo-fill" role="img" aria-label="Photo of a blood pressure check with a stethoscope on an arm" style="background:linear-gradient(135deg,#f1ddd0,#c99a82 55%,#6d6d6f)"></div>
</div>
<div class="card-frame" style="left:309px">
  <div class="photo-fill" role="img" aria-label="Street map showing the clinic location" style="background:linear-gradient(160deg,#eeeae3,#dcd8cf)"></div>
</div>
<div class="card-frame" style="left:590px">
  <div class="photo-fill" role="img" aria-label="Photo of a doctor holding a tablet with a glowing heart graphic" style="background:linear-gradient(180deg,#e6eef6,#a9c4dc 60%,#f0b27a)"></div>
</div>

<p class="caption" style="left:27px">at Crestline Heart we Strive to provide the highest level and Quality of cardiac care Available</p>
<p class="caption" style="left:306px">at Crestline Heart we Strive to provide the highest level and Quality of cardiac care Available</p>
<p class="caption" style="left:584px">at Crestline Heart we Strive to provide the highest level and Quality of cardiac care Available</p>

</body>
</html>
```